Company Stationary

I'd like a template to use for company stationery. We frequently write short 1 - 2 page Word documents (which we save as PDF) to clients and prospects and the presentation is boring and doesn't look professional. I am looking for a Word template that will convey a better sense of professionalism. The design should include our logo (attached) but be simple and elegant. It should save nicely as a PDF, since that is how we will send the files via email.

Target Market(s)

Financial Institutions

Industry/Entity Type

Financial Service

Font styles to use
Serif

Colors

Designer to choose colors to be used in the design.

Requirements
Must have
• Simple design. Needs to be subtle. I don't want the design to be more interesting than the message we are writing.
Nice to have
• When the reader sees it, I want them to feel they are reading something published by a large, very successful company.
Should not have
• Not overpowering design and colors.

```html
<!DOCTYPE html>
<html lang="en">
<head>
<meta charset="utf-8">
<title>Veritane Letterhead</title>
<link rel="stylesheet" href="https://fonts.googleapis.com/css2?family=Exo+2:wght@700&display=swap">
<style>
  :root {
    --paper: #ffffff;
    --accent-red: #ff0d00;
    --deep-maroon: #540200;
    --mark-ink: #0a0a0a;
  }
  html, body {
    margin: 0;
    padding: 0;
    overflow: hidden;
    background: var(--paper);
  }
  .letterhead {
    position: relative;
    width: 848px;
    height: 1200px;
    overflow: hidden;
    background: var(--paper);
  }
  .footer-wave {
    position: absolute;
    left: 0;
    top: 0;
    width: 848px;
    height: 1200px;
  }
  .wave-accent { fill: var(--accent-red); }
  .wave-base { fill: var(--deep-maroon); }
  .company-name {
    position: absolute;
    left: 24px;
    top: 1112px;
    margin: 0;
    font-family: "Exo 2", sans-serif;
    font-weight: 700;
    font-size: 58px;
    line-height: 1;
    letter-spacing: 1px;
    color: var(--mark-ink);
  }
</style>
</head>
<body>
  <main class="letterhead">
    <svg class="footer-wave" viewBox="0 0 848 1200" aria-hidden="true">
      <path class="wave-accent" d="M0,1040 C60,998 200,994 350,1040 S740,1122 848,1104 L848,1200 L0,1200 Z"/>
      <path class="wave-base" d="M0,1062 C70,1018 210,1020 355,1064 S750,1146 848,1128 L848,1200 L0,1200 Z"/>
    </svg>
    <p class="company-name">Veritane</p>
  </main>
</body>
</html>
```